Website for a service provided by a Canadian Immigration Company

Design and Code a website for a Canadian immigration company which provides service to clients all across the world. the website should be very Canadian centric and have 4-5 pages. Basic, classy modern. I have the logo s already designed. Please contact me and I can send you some more details. It's basically a service which is provided to clients who are below 17 and need a guardian in canada to sign their documents that they will be looked after them. It's called custodianship. You can google the term and you will understand what it means
Updates

didn't realize it was just a day

Target Market(s)

17-55

Industry/Entity Type

Immigration

Coding

Coded - Design and coding required

Number of Pages Required

5+ page

Font styles to use
Sans Serif

Colors
EE7325
F08F49
F5BC92
FAE3D3
FDF4ED
EB3D1F
EC4F4E
F09395
F8D3D4
FCEDEE

Requirements
Must have
• Pages with some graphics, some small animations like clients served, projects completed

```html
<!DOCTYPE html>
<html lang="en">
<head>
<meta charset="UTF-8">
<title>Maple Ward – Custodianship for International Students</title>
<link href="https://fonts.googleapis.com/css2?family=Montserrat:wght@600;700&family=Lato:wght@400;700&display=swap" rel="stylesheet">
<style>
:root{
  --red:#eb2127;
  --red-deep:#d81e24;
  --orange:#ee6a25;
  --orange-soft:#f08f49;
  --ink:#111111;
  --text:#333333;
  --grey-bg:#f0f0f0;
  --line:#dcdcdc;
  --white:#ffffff;
}
*{box-sizing:border-box;margin:0;padding:0}
html,body{width:1200px;height:3419px;overflow:hidden}
body{position:relative;background:var(--white);font-family:'Lato',sans-serif;color:var(--text)}
.abs{position:absolute}
h1,h2,h3,.btn,.brand{font-family:'Montserrat',sans-serif}
.btn{display:flex;align-items:center;justify-content:center;border-radius:30px;font-weight:700;text-transform:uppercase;color:var(--white);font-size:14px;text-decoration:none}

/* header */
.site-header{left:111px;top:24px;width:979px;height:69px;background:var(--white);border-radius:0 35px 35px 0}
.logo-tab{left:111px;top:0;width:128px;height:126px;background:var(--white);border-radius:0 0 64px 64px}
.brand{display:flex;align-items:center;gap:10px;font-weight:600;color:var(--ink)}
.brand-dot{width:30px;height:30px;border-radius:50%;background:var(--red)}
.header-brand{left:142px;top:38px;font-size:29px}
.main-nav{left:564px;top:48px;display:flex;gap:37px;font-size:15px;color:var(--ink)}
.btn-login{left:969px;top:35px;width:111px;height:45px;background:var(--red);text-transform:none;font-size:15px}

/* hero */
.hero-photo{left:0;top:0;width:1200px;height:683px;background:linear-gradient(180deg,#3d4f78 0%,#5a6f98 25%,#2a3550 45%,#3b3a45 65%,#4a3b3e 100%)}
.hero-shade{left:0;top:0;width:1200px;height:683px;background:linear-gradient(90deg,rgba(20,25,40,.55),rgba(20,25,40,0) 60%)}
.hero-kicker{left:115px;top:232px;font-size:29px;color:var(--red);font-weight:600;letter-spacing:.5px}
.hero-title{left:112px;top:266px;font-size:62px;color:var(--white);font-weight:700;letter-spacing:1px}
.hero-lead{left:115px;top:347px;width:460px;font-size:15px;line-height:26px;color:var(--white)}
.btn-start{left:113px;top:421px;width:146px;height:51px;background:var(--red);font-size:13px}
.hero-wave{left:0;top:560px}

/* what we do */
.wwd-photo{left:98px;top:732px;width:465px;height:465px;border-radius:50%;background:radial-gradient(circle at 40% 40%,#d9b89a,#8a6e58 55%,#b23033 85%)}
.wwd-title{left:591px;top:781px;font-size:41px;color:var(--ink);font-weight:700}
.wwd-text{left:591px;top:844px;width:500px;font-size:15px;line-height:26px;color:var(--text)}
.btn-learn{left:588px;top:1102px;width:151px;height:54px;background:var(--orange)}

/* services */
.services{left:0;top:1320px;width:1200px;height:617px;background:var(--grey-bg)}
.services-title{left:0;top:1372px;width:1200px;text-align:center;font-size:36px;color:var(--ink);font-weight:700}
.card{width:294px;height:404px;top:1456px;background:var(--white);border-radius:6px;text-align:center}
.card-photo{position:absolute;left:0;top:0;width:294px;height:174px;border-radius:0 0 147px 147px}
.card h3{position:absolute;top:202px;width:100%;font-size:23px;color:var(--ink);font-weight:600}
.card p{position:absolute;top:240px;left:25px;width:244px;font-size:15px;line-height:26px;color:var(--text)}
.card .arrow{position:absolute;left:136px;top:364px}
.card-bar{top:1860px;width:260px;height:10px;background:var(--line)}
.card-bar.active{background:var(--red)}
.slider-btn{top:1661px;width:38px;height:38px;border-radius:50%}
.slider-btn.prev{left:93px;background:#dedede}
.slider-btn.next{left:1058px;background:var(--orange)}

/* about */
.about{left:0;top:1937px;width:1200px;height:380px;background:linear-gradient(90deg,#ef7a3c,#ee6a25 50%,#ef7a3c)}
.about-title{left:0;top:1993px;width:1200px;text-align:center;font-size:36px;color:var(--white);font-weight:700}
.about-text{left:160px;top:2052px;width:880px;text-align:center;font-size:15px;line-height:26px;color:var(--white)}
.btn-about{left:522px;top:2182px;width:151px;height:55px;background:var(--white);color:var(--orange)}

/* contact */
.contact{left:0;top:2317px;width:1200px;height:700px;background:linear-gradient(180deg,#f7f7f7,#ececec)}
.contact-title{left:0;top:2403px;width:1200px;text-align:center;font-size:36px;color:var(--ink);font-weight:700}
.field{background:var(--white);font-size:13px;color:var(--text);padding:19px 22px}
.btn-submit{left:535px;top:2716px;width:145px;height:54px;background:var(--red);font-size:16px}

/* footer */
.footer-wave{left:0;top:2880px}
.footer{left:0;top:2960px;width:1200px;height:459px;background:#000}
.footer-brand{left:0;top:2992px;width:1200px;justify-content:center;color:var(--white);font-size:42px}
.footer-brand .brand-dot{width:44px;height:44px}
.footer-nav{left:0;top:3107px;width:1200px;display:flex;justify-content:center;gap:32px;font-size:13px;color:var(--white)}
.info{top:3176px;display:flex;gap:14px;color:var(--white);font-size:15px;line-height:24px}
.info-icon{width:46px;height:46px;border-radius:50%;background:var(--red);display:flex;align-items:center;justify-content:center;flex:none}
.copyright{left:0;top:3274px;width:1200px;text-align:center;font-size:14px;color:var(--white)}
.socials{left:0;top:3330px;width:1200px;display:flex;justify-content:center;gap:16px}
.socials span{width:31px;height:31px;border-radius:50%;background:var(--red)}
</style>
</head>
<body>

<!-- hero -->
<div class="abs hero-photo" role="img" aria-label="Evening view of a Canadian waterfront with a lit geodesic dome, city skyline and docked canoes"></div>
<div class="abs hero-shade"></div>
<svg class="abs hero-wave" width="1200" height="130" viewBox="0 0 1200 130">
  <path d="M0 8 C300 120 800 150 1200 10 L1200 130 L0 130 Z" fill="var(--red)"/>
  <path d="M0 8 C300 110 800 120 1200 60 L1200 130 L0 130 Z" fill="var(--white)"/>
</svg>

<div class="abs logo-tab"></div>
<div class="abs site-header"></div>
<div class="abs brand header-brand"><span class="brand-dot"></span>mapleward.ca</div>
<nav class="abs main-nav"><span>Home</span><span>About Us</span><span>Services</span><span>Contact Us</span></nav>
<a class="abs btn btn-login">Login</a>

<h2 class="abs hero-kicker">WELCOME TO</h2>
<h1 class="abs hero-title">MAPLE WARD</h1>
<p class="abs hero-lead">Lorem ipsum dolor sit amet, consectetur adipiscing elit, sed do eiusmod tempor incididunt ut labore et dolore</p>
<a class="abs btn btn-start">Get Started</a>

<!-- what we do -->
<div class="abs wwd-photo" role="img" aria-label="Smiling student in a beanie with a red maple-leaf graphic overlay"></div>
<h2 class="abs wwd-title">WHAT WE DO</h2>
<p class="abs wwd-text">We provide the required signed and notarized custodian declaration along with formal supervision service upon the student’s arrival in Canada. According to Citizenship and Immigration Canada (IRCC), minor students can be accepted at a university or college, but they cannot obtain a study permit without the required signed and notarized custodianship form. We provide support for minor international students and peace of mind for their parents. Our warm and kindhearted Legal Custodian will guide international students through their first challenging months in a new environment.</p>
<a class="abs btn btn-learn">Learn More</a>

<!-- services -->
<div class="abs services"></div>
<h2 class="abs services-title">OUR SERVICES</h2>

<div class="abs card" style="left:125px">
  <div class="card-photo" role="img" aria-label="Student studying at a café table" style="background:linear-gradient(135deg,#b9a89a,#6e5b4f)"></div>
  <h3>Lorem Ipsum</h3>
  <p>Lorem ipsum dolor sit amet, consectetur adipiscing elit, sed do eiusmod tempor incididunt ut labore et dolore magna aliqua.</p>
  <svg class="arrow" width="22" height="18" viewBox="0 0 22 18"><path d="M1 9H20M13 2l7 7-7 7" stroke="#999" stroke-width="2" fill="none"/></svg>
</div>
<div class="abs card" style="left:450px">
  <div class="card-photo" role="img" aria-label="Group of students walking outdoors in a park" style="background:linear-gradient(135deg,#9cc07a,#4f7a3c)"></div>
  <h3>Lorem Ipsum</h3>
  <p>Lorem ipsum dolor sit amet, consectetur adipiscing elit, sed do eiusmod tempor incididunt ut labore et dolore magna aliqua.</p>
  <svg class="arrow" width="22" height="18" viewBox="0 0 22 18"><path d="M1 9H20M13 2l7 7-7 7" stroke="var(--red)" stroke-width="2.5" fill="none"/></svg>
</div>
<div class="abs card" style="left:775px">
  <div class="card-photo" role="img" aria-label="Young woman talking with an older woman on a sofa" style="background:linear-gradient(135deg,#dcd6d0,#a89484)"></div>
  <h3>Lorem Ipsum</h3>
  <p>Lorem ipsum dolor sit amet, consectetur adipiscing elit, sed do eiusmod tempor incididunt ut labore et dolore magna aliqua.</p>
  <svg class="arrow" width="22" height="18" viewBox="0 0 22 18"><path d="M1 9H20M13 2l7 7-7 7" stroke="#999" stroke-width="2" fill="none"/></svg>
</div>
<div class="abs card-bar" style="left:142px"></div>
<div class="abs card-bar active" style="left:467px"></div>
<div class="abs card-bar" style="left:792px"></div>
<div class="abs slider-btn prev"><svg width="38" height="38"><path d="M21 14l-5 5 5 5" stroke="var(--red)" stroke-width="1.5" fill="none"/></svg></div>
<div class="abs slider-btn next"><svg width="38" height="38"><path d="M17 14l5 5-5 5" stroke="#fff" stroke-width="1.5" fill="none"/></svg></div>

<!-- about -->
<div class="abs about" role="img" aria-label="Students with backpacks, tinted orange"></div>
<h2 class="abs about-title">ABOUT US</h2>
<p class="abs about-text">Lorem ipsum dolor sit amet, consectetur adipiscing elit, sed do eiusmod tempor incididunt ut labore et dolore magna aliqua. Quis ipsum suspendisse ultrices gravida. Risus commodo viverra maecenas accumsan lacus vel facilisis. Lorem ipsum dolor sit amet, consectetur adipiscing elit, sed do eiusmod tempor incididunt ut labore et dolore magna aliqua. Quis ipsum suspendisse ultrices gravida. Risus commodo viverra maecenas accumsan lacus vel facilisis.</p>
<a class="abs btn btn-about">Learn More</a>

<!-- contact -->
<div class="abs contact"></div>
<h2 class="abs contact-title">CONTACT US</h2>
<div class="abs field" style="left:139px;top:2490px;width:302px;height:49px">Enter Name</div>
<div class="abs field" style="left:456px;top:2490px;width:302px;height:49px">Enter Email</div>
<div class="abs field" style="left:774px;top:2490px;width:301px;height:49px">Enter Phone</div>
<div class="abs field" style="left:139px;top:2558px;width:936px;height:125px">Message</div>
<a class="abs btn btn-submit">Submit</a>

<!-- footer -->
<svg class="abs footer-wave" width="1200" height="90" viewBox="0 0 1200 90">
  <path d="M0 80 C300 -10 800 -20 1200 70 L1200 90 L0 90 Z" fill="var(--red)"/>
  <path d="M0 90 C300 15 800 0 1200 80 L1200 90 Z" fill="#000"/>
</svg>
<div class="abs footer"></div>
<div class="abs brand footer-brand"><span class="brand-dot"></span>mapleward.ca</div>
<nav class="abs footer-nav"><span>Home</span><span>About Us</span><span>Services</span><span>Contact Us</span></nav>

<div class="abs info" style="left:218px">
  <div class="info-icon"><svg width="18" height="22" viewBox="0 0 18 22"><path d="M9 1a7 7 0 0 0-7 7c0 5 7 13 7 13s7-8 7-13a7 7 0 0 0-7-7z" fill="#fff"/><circle cx="9" cy="8" r="2.5" fill="var(--red)"/></svg></div>
  <div>Location<br>Maple Ward Toronto, Canada</div>
</div>
<div class="abs info" style="left:510px">
  <div class="info-icon"><svg width="20" height="20" viewBox="0 0 20 20"><path d="M4 1l4 4-2 3c1 2 3 4 5 5l3-2 4 4-2 3C9 18 2 11 1 4z" fill="#fff"/></svg></div>
  <div>Phone<br>+1 555 010 0199</div>
</div>
<div class="abs info" style="left:748px">
  <div class="info-icon"><svg width="20" height="14" viewBox="0 0 20 14"><rect width="20" height="14" rx="1" fill="#fff"/><path d="M1 1l9 7 9-7" stroke="var(--red)" stroke-width="1.5" fill="none"/></svg></div>
  <div>Email<br>info@mapleward.com</div>
</div>

<p class="abs copyright">© copyrights 2023 Maple Ward &nbsp;&nbsp;|&nbsp;&nbsp;&nbsp;&nbsp; All rights reserved.</p>
<div class="abs socials"><span></span><span></span><span></span><span></span></div>

</body>
</html>
```